CFO services graphic design

I own a business consulting firm called Marlowe Consulting and we need a graphic for CFO services in our colours and branding. The attached file "CFO services to be put into Marlowe consulting theme", shows the content for the design. The two other files show the theme and colours for the new design.

```html
<!DOCTYPE html>
<html lang="en">
<head>
<meta charset="UTF-8">
<title>Marlowe Consulting – CFO Services</title>
<link href="https://fonts.googleapis.com/css2?family=Open+Sans:wght@400;600;700&display=swap" rel="stylesheet">
<style>
  :root {
    --bg: #ffffff;
    --brand-navy: #1c2d4a;
    --brand-teal: #138f84;
    --brand-gold: #d9a11e;
    --teal-soft: #8ed6cc;
    --gold-soft: #f4d28c;
    --hub-fill: #f2f4f6;
    --hub-rim: #dadde2;
    --ink: var(--brand-navy);
  }
  html, body {
    margin: 0;
    padding: 0;
    width: 1200px;
    height: 1000px;
    overflow: hidden;
    background: var(--bg);
  }
  .canvas {
    position: relative;
    width: 1200px;
    height: 1000px;
    font-family: "Open Sans", Arial, sans-serif;
    color: var(--ink);
  }
  .wheel {
    position: absolute;
    inset: 0;
  }
  .segment-label {
    position: absolute;
    transform: translate(-50%, -50%);
    text-align: center;
    font-size: 17.5px;
    line-height: 22px;
    font-weight: 700;
    white-space: nowrap;
    margin: 0;
  }
  .segment-label .detail {
    font-weight: 400;
  }
  .hub-title {
    position: absolute;
    left: 600px;
    top: 500px;
    transform: translate(-50%, -50%);
    margin: 0;
    text-align: center;
    font-size: 30px;
    line-height: 36px;
    font-weight: 700;
    letter-spacing: 0.5px;
    color: var(--ink);
  }
  .brand-mark {
    position: absolute;
    left: 600px;
    top: 950px;
    transform: translate(-50%, -50%);
    display: flex;
    align-items: center;
    gap: 10px;
    margin: 0;
    font-size: 16px;
    font-weight: 600;
    color: var(--brand-navy);
    white-space: nowrap;
  }
  .brand-dot {
    width: 12px;
    height: 12px;
    border-radius: 50%;
    background: var(--brand-teal);
  }
</style>
</head>
<body>
<main class="canvas">
  <svg class="wheel" width="1200" height="1000" viewBox="0 0 1200 1000" aria-hidden="true">
    <defs>
      <filter id="hub-shadow" x="-20%" y="-20%" width="140%" height="140%">
        <feDropShadow dx="0" dy="2" stdDeviation="4" flood-color="#000" flood-opacity="0.18"/>
      </filter>
    </defs>
    <g class="segments">
      <path fill="var(--teal-soft)" d="M600 500 L600 100 A400 400 0 0 1 882.84 217.16 Z"/>
      <path fill="var(--gold-soft)" d="M600 500 L882.84 217.16 A400 400 0 0 1 1000 500 Z"/>
      <path fill="var(--teal-soft)" d="M600 500 L1000 500 A400 400 0 0 1 882.84 782.84 Z"/>
      <path fill="var(--gold-soft)" d="M600 500 L882.84 782.84 A400 400 0 0 1 600 900 Z"/>
      <path fill="var(--teal-soft)" d="M600 500 L600 900 A400 400 0 0 1 317.16 782.84 Z"/>
      <path fill="var(--gold-soft)" d="M600 500 L317.16 782.84 A400 400 0 0 1 200 500 Z"/>
      <path fill="var(--teal-soft)" d="M600 500 L200 500 A400 400 0 0 1 317.16 217.16 Z"/>
      <path fill="var(--gold-soft)" d="M600 500 L317.16 217.16 A400 400 0 0 1 600 100 Z"/>
    </g>
    <g class="inner-ring">
      <path fill="var(--brand-teal)" d="M600 500 L600 350 A150 150 0 0 1 706.07 393.93 Z"/>
      <path fill="var(--brand-gold)" d="M600 500 L706.07 393.93 A150 150 0 0 1 750 500 Z"/>
      <path fill="var(--brand-teal)" d="M600 500 L750 500 A150 150 0 0 1 706.07 606.07 Z"/>
      <path fill="var(--brand-gold)" d="M600 500 L706.07 606.07 A150 150 0 0 1 600 650 Z"/>
      <path fill="var(--brand-teal)" d="M600 500 L600 650 A150 150 0 0 1 493.93 606.07 Z"/>
      <path fill="var(--brand-gold)" d="M600 500 L493.93 606.07 A150 150 0 0 1 450 500 Z"/>
      <path fill="var(--brand-teal)" d="M600 500 L450 500 A150 150 0 0 1 493.93 393.93 Z"/>
      <path fill="var(--brand-gold)" d="M600 500 L493.93 393.93 A150 150 0 0 1 600 350 Z"/>
    </g>
    <g class="dividers" stroke="var(--bg)" stroke-width="30">
      <line x1="600" y1="80" x2="600" y2="920"/>
      <line x1="180" y1="500" x2="1020" y2="500"/>
      <line x1="303" y1="203" x2="897" y2="797"/>
      <line x1="897" y1="203" x2="303" y2="797"/>
    </g>
    <circle class="hub" cx="600" cy="500" r="118" fill="var(--hub-fill)" stroke="var(--hub-rim)" stroke-width="8" filter="url(#hub-shadow)"/>
    <path class="hub-arc-top" d="M506 472 A96 96 0 0 1 694 472" fill="none" stroke="var(--brand-gold)" stroke-width="10"/>
    <path class="hub-arc-bottom" d="M506 528 A96 96 0 0 0 694 528" fill="none" stroke="var(--brand-teal)" stroke-width="10"/>
  </svg>

  <h1 class="hub-title">CHIEF<br>FINANCIAL<br>OFFICER</h1>

  <p class="segment-label" style="left:476px; top:232px;">Cost Accounting &amp;<br>Cost Management</p>
  <p class="segment-label" style="left:723px; top:232px;">Capital Structure &amp;<br>The Cost of Capital</p>
  <p class="segment-label" style="left:858px; top:416px;">Long-term &amp; Short-term<br>Investment Decisions</p>
  <p class="segment-label" style="left:858px; top:600px;">Performance<br>Evaluation</p>
  <p class="segment-label" style="left:723px; top:765px;">Budgeting &amp;<br>Strategic Planning</p>
  <p class="segment-label" style="left:476px; top:765px;">Risk<br>Management</p>
  <p class="segment-label" style="left:330px; top:597px;">Compliance:<br>Tax, Legal and<br>Regulator</p>
  <p class="segment-label" style="left:327px; top:404px;">Communication:<br><span class="detail">Board of Directors,<br>Creditors, Owners,<br>Investors, Credit<br>Rating Agencies</span></p>

  <p class="brand-mark"><span class="brand-dot"></span>Marlowe Consulting</p>
</main>
</body>
</html>
```